Email Signature & Facebook Cover Design – Birchlane Study Centre

I’m looking for a clean, professional email signature and a matching Facebook cover photo for my tutoring business, Birchlane Study Centre.
The email signature needs to display properly across Outlook and iPhone without the image appearing as an attachment. It should include my logo and contact details and have a friendly but professional look suitable for an education business.
Details to include:
Moira Dunholt
Director & Lead Tutor
Birchlane Study Centre
hello@birchlanestudy.co.uk
www.birchlanestudy.co.uk
01632 418736
The Facebook cover should match the branding, feel professional and welcoming, and be optimised for desktop and mobile.

```html
<!DOCTYPE html>
<html lang="en">
<head>
<meta charset="utf-8">
<title>Birchlane Study Centre – Email Signature &amp; Cover</title>
<link href="https://fonts.googleapis.com/css2?family=Lexend:wght@400;500;600&display=swap" rel="stylesheet">
<style>
  :root {
    --stage: #dcdcdd;
    --paper: #ffffff;
    --green: #4fae60;
    --green-deep: #3c9a4f;
    --green-band: #3a914a;
    --green-text: #2f7d46;
    --ink: #22343a;
    --lime: #d6ef7c;
    --pale: #eef6ea;
  }
  * { box-sizing: border-box; margin: 0; padding: 0; }
  html, body { width: 1200px; height: 800px; overflow: hidden; }
  body {
    background: var(--stage);
    font-family: "Lexend", sans-serif;
    position: relative;
  }
  .signature, .cover {
    position: absolute;
    overflow: hidden;
    box-shadow: 0 2px 6px rgba(0,0,0,0.12);
  }
  .signature { left: 133px; top: 72px; width: 932px; height: 262px; background: var(--paper); }
  .cover { left: 134px; top: 378px; width: 930px; height: 313px; background: var(--green); }
  .backdrop { position: absolute; inset: 0; }

  .signature__name { position: absolute; left: 34px; top: 30px; font-size: 30px; font-weight: 500; color: var(--ink); }
  .signature__role { position: absolute; left: 34px; top: 74px; font-size: 21px; color: var(--green-text); }
  .signature__rule { position: absolute; left: 34px; top: 111px; width: 372px; height: 3px;
    background: linear-gradient(90deg, var(--green-text) 60%, rgba(47,125,70,0)); }
  .contact-list { position: absolute; left: 34px; top: 134px; list-style: none; }
  .contact-list li { display: flex; align-items: center; height: 37px; font-size: 20px; color: var(--green-text); }
  .contact-list svg { width: 26px; height: 22px; margin-right: 14px; }

  .pencil-art { position: absolute; left: 390px; top: 140px; width: 190px; height: 34px;
    border-radius: 12px; transform: rotate(-38deg);
    background: linear-gradient(90deg, #e6f39a, #bfe58a); }

  .brand-name { position: absolute; color: var(--paper); font-weight: 600; line-height: 1.05; }
  .signature .brand-name { left: 640px; top: 70px; width: 250px; text-align: center; font-size: 36px; }

  .cover__photo { position: absolute; left: 0; top: 0; width: 250px; height: 313px;
    background: linear-gradient(160deg, #c9cbb8, #a7bfa2 55%, #bcdcc0);
    clip-path: path("M0 0 H232 C262 90 268 210 244 313 H0 Z"); }
  .cover .brand-name { left: 341px; top: 70px; font-size: 42px; }
  .cover__tagline { position: absolute; left: 341px; top: 138px; font-size: 22px; font-weight: 500; color: var(--paper); }
  .cover__band { position: absolute; left: 241px; top: 251px; right: 0; height: 62px; background: var(--green-band); }
  .cover__contacts { position: absolute; left: 266px; top: 266px; display: flex; align-items: center; gap: 14px;
    font-size: 20px; color: var(--paper); }
  .cover__contacts svg { width: 26px; height: 22px; }
  .cover__contacts .gap { width: 4px; }
  .books-art { position: absolute; left: 800px; top: 172px; width: 130px; height: 122px;
    border-radius: 10px 0 0 10px; background: linear-gradient(180deg, #f0b04a, #e8c85a 45%, #3f8f4a); }
</style>
</head>
<body>

<section class="signature" aria-label="Email signature">
  <svg class="backdrop" viewBox="0 0 932 262" aria-hidden="true">
    <defs>
      <linearGradient id="sigFade" x1="0" x2="1">
        <stop offset="0" stop-color="#ffffff"/>
        <stop offset="1" stop-color="#e2f1dc"/>
      </linearGradient>
    </defs>
    <rect width="932" height="262" fill="url(#sigFade)"/>
    <path d="M520 0 H932 V262 H440 C520 220 580 120 540 0 Z" fill="#bfe0b3"/>
    <path d="M562 0 H932 V262 H454 C560 215 600 110 562 0 Z" fill="var(--green)"/>
  </svg>
  <h1 class="signature__name">Moira Dunholt</h1>
  <p class="signature__role">Director &amp; Lead Tutor</p>
  <div class="signature__rule"></div>
  <ul class="contact-list">
    <li><svg viewBox="0 0 26 20"><rect x="0" y="1" width="26" height="18" rx="2" fill="var(--green-text)"/><path d="M1 3 L13 12 L25 3" stroke="#fff" stroke-width="2" fill="none"/></svg><span><b style="font-weight:600">hello</b>@birchlanestudy.co.uk</span></li>
    <li><svg viewBox="0 0 24 24"><g fill="none" stroke="var(--green-text)" stroke-width="2"><circle cx="12" cy="12" r="10"/><ellipse cx="12" cy="12" rx="4.5" ry="10"/><path d="M2 12 H22 M4 7 H20 M4 17 H20"/></g></svg><span>www.birchlanestudy.co.uk</span></li>
    <li><svg viewBox="0 0 24 24"><path d="M6.6 10.8a15.1 15.1 0 0 0 6.6 6.6l2.2-2.2a1 1 0 0 1 1-.25 11.4 11.4 0 0 0 3.6.57 1 1 0 0 1 1 1V20a1 1 0 0 1-1 1A17 17 0 0 1 3 4a1 1 0 0 1 1-1h3.5a1 1 0 0 1 1 1c0 1.25.2 2.45.57 3.57a1 1 0 0 1-.25 1z" fill="var(--green-text)"/></svg><span>01632 418736</span></li>
  </ul>
  <div class="pencil-art" role="img" aria-label="Illustration of a pale green pencil"></div>
  <p class="brand-name">Birchlane<br>Study Centre</p>
</section>

<section class="cover" aria-label="Facebook cover">
  <svg class="backdrop" viewBox="0 0 930 313" aria-hidden="true">
    <defs>
      <radialGradient id="coverGlow" cx="0.35" cy="0.8" r="0.6">
        <stop offset="0" stop-color="#8fd060"/>
        <stop offset="1" stop-color="var(--green)"/>
      </radialGradient>
    </defs>
    <rect width="930" height="313" fill="url(#coverGlow)"/>
    <path d="M232 0 C262 90 268 210 244 313" stroke="#a6de7a" stroke-width="10" fill="none"/>
  </svg>
  <div class="cover__photo" role="img" aria-label="Portrait photo of the lead tutor in front of bookshelves"></div>
  <p class="brand-name">Birchlane Study Centre</p>
  <p class="cover__tagline">Helping Students Achieve Their Best</p>
  <div class="cover__band"></div>
  <div class="books-art" role="img" aria-label="Illustration of stacked books, pencils and an apple"></div>
  <div class="cover__contacts">
    <svg viewBox="0 0 26 20"><rect x="0" y="1" width="26" height="18" rx="2" fill="var(--lime)"/><path d="M1 3 L13 12 L25 3" stroke="var(--green-band)" stroke-width="2" fill="none"/></svg>
    <span>hello@birchlanestudy.co.uk</span>
    <span class="gap"></span>
    <svg viewBox="0 0 24 24"><path d="M6.6 10.8a15.1 15.1 0 0 0 6.6 6.6l2.2-2.2a1 1 0 0 1 1-.25 11.4 11.4 0 0 0 3.6.57 1 1 0 0 1 1 1V20a1 1 0 0 1-1 1A17 17 0 0 1 3 4a1 1 0 0 1 1-1h3.5a1 1 0 0 1 1 1c0 1.25.2 2.45.57 3.57a1 1 0 0 1-.25 1z" fill="var(--lime)"/></svg>
    <span>01632 418736</span>
  </div>
</section>

</body>
</html>
```